Gemstone Jewelry Online Shop Needs a Banner Design

We need a banner design for a new gemstone Jewelry Online Shop based in the U.S. called "Lumorra". One of our selling points is "never fall out of stone". We want to express: a Party Queen doesn't need to worry whenever she may meet an embarrassing moment - a stone of jewelry falls out at a very important occasion. Please insert one of attached images. Please visit our website for more details: http://lumorra-example.com/
The banner size: 1200*628
If you think other images at our website are better, please let us know. Many thanks and looking forward to your beautiful and creative designs!

Industry/Entity Type

Jewelry

```html
<!DOCTYPE html>
<html lang="en">
<head>
<meta charset="utf-8">
<title>Lumorra – Never Fall Out of Stone</title>
<link rel="stylesheet" href="https://fonts.googleapis.com/css2?family=Didact+Gothic&display=swap">
<style>
  :root {
    --bg-core: #b3070c;
    --bg-mid: #8f0309;
    --bg-edge: #4e0105;
    --facet: rgba(255, 255, 255, 0.06);
    --facet-dark: rgba(60, 0, 4, 0.35);
    --headline-top: #f4f4f4;
    --headline-bottom: #b4b4b4;
    --button-fill: #d80f16;
    --button-fill-dark: #b9070d;
    --button-text: #ffffff;
    --ring-silver: #eeeef2;
    --ring-silver-shade: #b9b9c2;
    --ring-garnet: #c0141e;
    --ring-garnet-dark: #6a0309;
  }
  * { margin: 0; padding: 0; box-sizing: border-box; }
  html, body {
    width: 1200px;
    height: 628px;
    overflow: hidden;
    background: var(--bg-edge);
  }
  .banner {
    position: relative;
    width: 1200px;
    height: 628px;
    overflow: hidden;
    background: radial-gradient(ellipse 620px 420px at 560px 300px, var(--bg-core) 0%, var(--bg-mid) 55%, var(--bg-edge) 100%);
    font-family: "Didact Gothic", "Century Gothic", sans-serif;
  }
  .banner__facets, .headline, .cta__label {
    position: absolute;
    left: 0;
    top: 0;
  }
  .headline text {
    font-family: "Didact Gothic", "Century Gothic", sans-serif;
    font-size: 52px;
    text-transform: uppercase;
  }
  .cta {
    position: absolute;
    left: 116px;
    top: 367px;
    width: 222px;
    height: 64px;
    border-radius: 3px;
    background: linear-gradient(180deg, var(--button-fill) 0%, var(--button-fill-dark) 100%);
    text-decoration: none;
  }
  .cta text {
    font-family: "Didact Gothic", "Century Gothic", sans-serif;
    font-size: 27px;
    fill: var(--button-text);
  }
  .cta--reflection {
    top: 433px;
    transform: scaleY(-1);
    opacity: 0.12;
    -webkit-mask-image: linear-gradient(0deg, #000 0%, transparent 60%);
    mask-image: linear-gradient(0deg, #000 0%, transparent 60%);
  }
  .product-photo {
    position: absolute;
    left: 660px;
    top: 108px;
    width: 350px;
    height: 378px;
    border-radius: 50%;
    background:
      radial-gradient(ellipse 62px 58px at 50% 40%, var(--ring-garnet) 0%, var(--ring-garnet-dark) 96%, var(--ring-silver) 100%),
      radial-gradient(ellipse at 50% 40%, var(--ring-silver) 0%, var(--ring-silver-shade) 100%);
    box-shadow: 0 0 0 10px var(--ring-garnet-dark) inset, 0 6px 18px rgba(0, 0, 0, 0.35);
  }
  .product-reflection {
    position: absolute;
    left: 725px;
    top: 500px;
    width: 270px;
    height: 110px;
    border-radius: 50%;
    background: radial-gradient(ellipse at 50% 30%, rgba(233, 233, 238, 0.16) 0%, transparent 70%);
  }
</style>
</head>
<body>
  <main class="banner">
    <svg class="banner__facets" width="1200" height="628" viewBox="0 0 1200 628" aria-hidden="true">
      <polygon points="95,150 330,80 250,330" fill="var(--facet)"/>
      <polygon points="250,330 330,80 380,300" fill="var(--facet-dark)"/>
      <polygon points="0,470 180,400 120,628 0,628" fill="var(--facet-dark)"/>
      <polygon points="180,400 300,470 230,628 120,628" fill="var(--facet)"/>
    </svg>

    <svg class="headline" width="1200" height="628" viewBox="0 0 1200 628" role="heading" aria-level="1" aria-label="Never Fall Out of Stone">
      <defs>
        <linearGradient id="headline-fill" x1="0" y1="0" x2="0" y2="1">
          <stop offset="0" stop-color="var(--headline-top)"/>
          <stop offset="1" stop-color="var(--headline-bottom)"/>
        </linearGradient>
      </defs>
      <text x="117" y="231" textLength="328" lengthAdjust="spacingAndGlyphs" fill="url(#headline-fill)">Never Fall</text>
      <text x="117" y="304" textLength="413" lengthAdjust="spacingAndGlyphs" fill="url(#headline-fill)">Out of Stone</text>
    </svg>

    <a class="cta" href="http://lumorra-example.com/">
      <svg class="cta__label" width="222" height="64" viewBox="0 0 222 64">
        <text x="23" y="43" textLength="176" lengthAdjust="spacingAndGlyphs">SHOP NOW</text>
      </svg>
    </a>
    <div class="cta cta--reflection" aria-hidden="true">
      <svg class="cta__label" width="222" height="64" viewBox="0 0 222 64">
        <text x="23" y="43" textLength="176" lengthAdjust="spacingAndGlyphs">SHOP NOW</text>
      </svg>
    </div>

    <div class="product-photo" role="img" aria-label="Product photo: silver flower ring set with a large oval red garnet, a halo of small white stones and eight pear-shaped garnet petals"></div>
    <div class="product-reflection" aria-hidden="true"></div>
  </main>
</body>
</html>
```